Ketto Athletics Packaging Design

We need a packaging design for a new company based in San Diego call KETTO ATHLETICS. We develop high quality custom sportswear through California and nationwide. We don't have any ideas we would like to see options, but the final design should communicate innovation and quality, basically we want our product to look professional and expensive

I upload our logo and the box die cut so you can use it.
Updates

Project Deadline Extended
Reason: We would like to see more options.

Target Market(s)

Retail Sportswear

Industry/Entity Type

It Company

Requirements
Must have
• Ketto athlettics logo and use our font (I upload it)
Nice to have
• We want the spearhead to be large

```html
<!DOCTYPE html>
<html lang="en">
<head>
<meta charset="utf-8">
<title>Ketto Athletics – Box Dieline</title>
<link rel="stylesheet" href="https://fonts.googleapis.com/css2?family=Michroma&family=Roboto:wght@500;700&display=swap">
<style>
  :root {
    --canvas: #ffffff;
    --charcoal: #2c2d2f;
    --charcoal-soft: #3b3c3f;
    --flap-dark: #3a3a3a;
    --flap-line: #4c4c4c;
    --band-grey: #6b6c6e;
    --label-grey: #747577;
    --ink: #1e1f21;
    --accent: #33b5e5;
    --accent-deep: #1689bd;
    --fold: rgba(255,255,255,0.38);
    --cut: #8a8a8a;
  }
  html, body {
    margin: 0;
    width: 1200px;
    height: 900px;
    overflow: hidden;
    background: var(--canvas);
  }
  .canvas {
    position: relative;
    width: 1200px;
    height: 900px;
  }
  .dieline {
    position: absolute;
    left: 150px;
    top: 480px;
    width: 870px;
    height: 382px;
  }
  .print-area {
    position: absolute;
    left: 0; top: 0;
    width: 870px;
    height: 285px;
    background:
      radial-gradient(ellipse 110px 120px at 95px 200px, rgba(51,181,229,0.75), rgba(22,137,189,0.35) 60%, transparent 100%),
      radial-gradient(ellipse 90px 100px at 665px 215px, rgba(51,181,229,0.7), rgba(22,137,189,0.3) 60%, transparent 100%),
      radial-gradient(ellipse 45px 45px at 755px 150px, rgba(51,181,229,0.55), transparent 100%),
      radial-gradient(ellipse 50px 40px at 825px 255px, rgba(51,181,229,0.55), transparent 100%),
      radial-gradient(ellipse 50px 50px at 530px 265px, rgba(51,181,229,0.55), transparent 100%),
      repeating-linear-gradient(90deg, rgba(51,181,229,0.10) 0 14px, transparent 14px 38px),
      repeating-linear-gradient(0deg, rgba(255,255,255,0.035) 0 16px, transparent 16px 34px),
      linear-gradient(160deg, var(--charcoal-soft), var(--charcoal) 65%);
  }
  .bottom-flaps {
    position: absolute;
    left: 0; top: 285px;
    width: 870px;
    height: 97px;
    background: var(--flap-dark);
  }
  .bottom-flap {
    position: absolute;
    top: 3px;
    height: 90px;
    border: 1px solid var(--flap-line);
    box-sizing: border-box;
  }
  .fold-h {
    position: absolute;
    left: 0;
    width: 870px;
    border-top: 1px dashed var(--fold);
  }
  .fold-v {
    position: absolute;
    top: 0;
    height: 382px;
    border-left: 1px solid rgba(255,255,255,0.10);
  }
  .glue-flap {
    position: absolute;
    left: 870px;
    top: 97px;
  }
  .brand {
    font-family: "Michroma", sans-serif;
    color: var(--ink);
    letter-spacing: 0.08em;
    margin: 0;
    white-space: nowrap;
  }
  .top-logo {
    position: absolute;
    left: 190px;
    top: 20px;
    width: 117px;
    height: 30px;
    background: var(--label-grey);
    border-radius: 4px 15px 15px 4px;
    display: flex;
    align-items: center;
    justify-content: center;
  }
  .top-logo .brand { font-size: 13px; }
  .category-label {
    position: absolute;
    left: 435px;
    top: 98px;
    width: 180px;
    height: 52px;
  }
  .category-label svg { position: absolute; inset: 0; }
  .category-label .category {
    position: absolute;
    top: 10px;
    width: 100%;
    text-align: center;
    font-family: "Michroma", sans-serif;
    color: var(--accent);
    font-size: 11px;
    letter-spacing: 0.08em;
    margin: 0;
  }
  .category-label .brand {
    position: absolute;
    top: 28px;
    width: 100%;
    text-align: center;
    font-size: 11px;
  }
  .name-band {
    position: absolute;
    left: 175px;
    top: 217px;
    width: 400px;
    height: 68px;
    background: var(--band-grey);
  }
  .name-band .brand {
    position: absolute;
    left: 20px;
    width: 220px;
    top: 17px;
    text-align: center;
    font-size: 26px;
    letter-spacing: 0.1em;
  }
  .tagline {
    position: absolute;
    left: 270px;
    top: 22px;
    font-family: "Roboto", sans-serif;
    font-weight: 500;
    color: var(--ink);
    font-size: 10px;
    line-height: 1.1;
    margin: 0;
  }
  .tagline span {
    display: block;
    padding-left: 35px;
    font-size: 11px;
    font-weight: 700;
  }
</style>
</head>
<body>
<main class="canvas">
  <section class="dieline" aria-label="Ketto Athletics box dieline">
    <div class="print-area" role="img" aria-label="All-over pattern of small blue and grey faceted triangles on dark charcoal, with large blue faceted accents"></div>

    <div class="bottom-flaps">
      <div class="bottom-flap" style="left:3px;width:181px"></div>
      <div class="bottom-flap" style="left:190px;width:240px"></div>
      <div class="bottom-flap" style="left:436px;width:179px"></div>
      <div class="bottom-flap" style="left:621px;width:246px"></div>
    </div>

    <div class="fold-h" style="top:97px"></div>
    <div class="fold-h" style="top:285px"></div>
    <div class="fold-v" style="left:187px"></div>
    <div class="fold-v" style="left:433px"></div>
    <div class="fold-v" style="left:618px"></div>

    <svg class="glue-flap" width="14" height="190" viewBox="0 0 14 190" aria-hidden="true">
      <path d="M0 0 L10 4 L10 184 L0 188" fill="none" stroke="var(--cut)" stroke-width="1"/>
    </svg>

    <div class="top-logo"><p class="brand">KETTO</p></div>

    <div class="category-label">
      <svg width="180" height="52" viewBox="0 0 180 52" aria-hidden="true">
        <polygon points="0,0 180,0 158,52 22,52" fill="var(--label-grey)"/>
      </svg>
      <p class="category">ATHLETICS</p>
      <p class="brand">KETTO</p>
    </div>

    <div class="name-band">
      <p class="brand">KETTO</p>
      <p class="tagline">Performance<span>Innovation</span></p>
    </div>
  </section>
</main>
</body>
</html>
```